Maple Ridge business card design

Card needs to include the following text/items:
Company Logo
Tobin Marsh
Phone # - 555-318-7642
service@mapleridgelandscaping.example
Lawn & landscape maintenance services

```html
<!DOCTYPE html>
<html lang="en">
<head>
<meta charset="utf-8">
<title>Maple Ridge Landscaping – Business Card</title>
<link rel="stylesheet" href="https://fonts.googleapis.com/css2?family=Open+Sans:ital,wght@0,400;0,800;1,700&display=swap">
<style>
  :root {
    --backdrop: #cbcbcb;
    --mint: #eefde0;
    --grass: #66aa00;
    --grass-light: #77bb0c;
    --forest: #1e630c;
    --ink: #1b5a0b;
  }
  * { margin: 0; padding: 0; box-sizing: border-box; }
  html, body {
    width: 1200px; height: 846px; overflow: hidden;
    background: var(--backdrop);
    font-family: "Open Sans", Arial, sans-serif;
  }
  .card {
    position: absolute; left: 346px;
    width: 508px; height: 290px; overflow: hidden;
  }
  .card-front { top: 113px; background: var(--mint); }
  .card-back { top: 443px; background: var(--grass); }

  .lawn-scene {
    position: absolute; left: 0; right: 0; top: 224px; bottom: 0;
    background: linear-gradient(90deg, var(--grass) 0%, var(--grass-light) 60%, var(--forest) 100%);
  }

  .brand {
    position: absolute; left: 52px; top: 47px; width: 200px;
    text-align: center; color: var(--forest);
  }
  .brand-mark {
    display: block; width: 104px; height: 104px; margin: 0 auto 8px;
    border-radius: 50%; background: var(--grass);
  }
  .brand-name {
    font-weight: 800; font-size: 26px; line-height: 1; letter-spacing: 0.3px;
  }

  .service-tiles { position: absolute; inset: 0; width: 100%; height: 100%; }

  .services {
    position: absolute; left: 47px; top: 34px;
    color: var(--ink); font-weight: 800; font-size: 25.5px;
    line-height: 29px; text-transform: uppercase;
  }
  .contact { position: absolute; left: 47px; top: 180px; color: var(--ink); }
  .contact-name { font-style: italic; font-weight: 700; font-size: 20px; line-height: 26px; margin-bottom: 2px; }
  .contact-line {
    display: flex; align-items: center; gap: 6px;
    font-size: 15.5px; line-height: 20px;
  }
  .contact-line svg { width: 12px; height: 12px; flex: none; }
  .icon-fill { fill: var(--ink); }
  .icon-fold { fill: none; stroke: var(--grass); stroke-width: 2; }
</style>
</head>
<body>

<section class="card card-front">
  <div class="lawn-scene" role="img" aria-label="Illustration of a winding lawn with a dirt path"></div>
  <div class="brand">
    <span class="brand-mark" aria-hidden="true"></span>
    <div class="brand-name">Maple Ridge</div>
  </div>
</section>

<section class="card card-back">
  <svg class="service-tiles" viewBox="0 0 972 555" preserveAspectRatio="none" role="img" aria-label="Four service tiles: lawn mowing, hedge trimming, leaf blowing and planting">
    <g fill="var(--forest)">
      <rect x="656" y="99" width="130" height="130" rx="22" transform="rotate(45 721 164)"/>
      <rect x="545" y="210" width="130" height="130" rx="22" transform="rotate(45 610 275)"/>
      <rect x="767" y="210" width="130" height="130" rx="22" transform="rotate(45 832 275)"/>
      <rect x="656" y="321" width="130" height="130" rx="22" transform="rotate(45 721 386)"/>
    </g>
  </svg>
  <h1 class="services">Lawn &amp;<br>Landscape<br>Maintenance<br>Services</h1>
  <div class="contact">
    <p class="contact-name">Tobin Marsh</p>
    <p class="contact-line">
      <svg viewBox="0 0 24 24" aria-hidden="true"><path class="icon-fill" d="M6.6 10.8c1.4 2.8 3.8 5.1 6.6 6.6l2.2-2.2c.3-.3.7-.4 1-.2 1.1.4 2.3.6 3.6.6.6 0 1 .4 1 1V20c0 .6-.4 1-1 1C10.6 21 3 13.4 3 4c0-.6.4-1 1-1h3.5c.6 0 1 .4 1 1 0 1.3.2 2.5.6 3.6.1.3 0 .7-.2 1z"/></svg>
      555-318-7642
    </p>
    <p class="contact-line">
      <svg viewBox="0 0 24 24" aria-hidden="true"><rect class="icon-fill" x="1" y="5" width="22" height="14"/><path class="icon-fold" d="M1 5l11 8 11-8"/></svg>
      service@mapleridgelandscaping.example
    </p>
  </div>
</section>

</body>
</html>
```